Ireland’s Oldest Thatched Pub. Irish Poítín Label

The Larchmoor Inn is a Ireland’s Oldest Thatched Pub dating back to 1654.
We Previously has launched our own Irish Whiskey under the brand name “Larchmoor 1712” Single Malt Irish Whiskey.
We are now planning to launch our own Irish Poítín and would like a bottle label designed. I have attached images of our Whiskey labels and images if the finished bottle.

```html
<!DOCTYPE html>
<html lang="en">
<head>
<meta charset="utf-8">
<title>Larchmoor 1712 Irish Poítín Label</title>
<link rel="stylesheet" href="https://fonts.googleapis.com/css2?family=Smokum&family=Ultra&family=Crimson+Text:wght@400;600;700&display=swap">
<style>
  :root {
    --backdrop: #797979;
    --frame-gold: #f4c33c;
    --label-cream: #fae096;
    --ink: #111111;
    --seal-red: #d01a0a;
  }
  html, body {
    margin: 0;
    padding: 0;
    overflow: hidden;
  }
  body {
    width: 1046px;
    height: 1200px;
    background: var(--backdrop);
    position: relative;
  }
  .label {
    position: absolute;
    left: 85px;
    top: 77px;
    width: 877px;
    height: 1045px;
    background: var(--frame-gold);
  }
  .label-panel {
    position: absolute;
    left: 17px;
    top: 18px;
    right: 20px;
    bottom: 16px;
    background: var(--label-cream);
  }
  .seal-tab {
    position: absolute;
    left: 377px;
    top: 0;
    width: 123px;
    height: 116px;
    background: var(--seal-red);
    border-radius: 0 0 61px 61px / 0 0 16px 16px;
  }
  .brand-arc {
    position: absolute;
    left: 0;
    top: 0;
    width: 877px;
    height: 400px;
  }
  .brand-arc text {
    font-family: "Smokum", "Rye", serif;
    font-size: 168px;
    fill: var(--ink);
  }
  .year {
    position: absolute;
    left: 0;
    width: 877px;
    top: 346px;
    margin: 0;
    text-align: center;
    font-family: "Ultra", "Abril Fatface", serif;
    font-weight: 400;
    font-size: 48px;
    line-height: 1;
    letter-spacing: 2px;
    color: var(--ink);
  }
  .spirit-name {
    position: absolute;
    left: 0;
    width: 877px;
    top: 428px;
    margin: 0;
    text-align: center;
    font-family: "Crimson Text", serif;
    font-weight: 600;
    font-size: 62px;
    line-height: 1;
    color: var(--seal-red);
  }
  .inn-scene {
    position: absolute;
    left: 64px;
    top: 514px;
    width: 745px;
    height: 393px;
    background: linear-gradient(180deg, #1a1a16 0%, #111 55%, #6b5f3e 78%, var(--label-cream) 100%);
  }
  .rule {
    position: absolute;
    left: 64px;
    top: 935px;
    width: 748px;
    height: 5px;
    background: var(--ink);
  }
  .company-name,
  .company-place {
    position: absolute;
    left: 0;
    width: 877px;
    margin: 0;
    text-align: center;
    font-family: "Crimson Text", serif;
    color: var(--ink);
    line-height: 1;
    white-space: nowrap;
  }
  .company-name {
    top: 947px;
    font-size: 24px;
    letter-spacing: 7px;
  }
  .company-place {
    top: 977px;
    font-size: 32px;
    font-weight: 700;
    letter-spacing: 4px;
  }
  .shamrock {
    position: absolute;
    top: 955px;
    width: 56px;
    height: 56px;
  }
  .shamrock.left { left: 64px; }
  .shamrock.right { left: 757px; }
</style>
</head>
<body>
  <div class="label">
    <div class="label-panel"></div>
    <div class="seal-tab"></div>

    <svg class="brand-arc" viewBox="0 0 877 400" aria-label="Larchmoor">
      <path id="brand-curve" d="M 110 366 Q 438 200 768 366" fill="none"/>
      <text text-anchor="middle">
        <textPath href="#brand-curve" startOffset="50%" textLength="650" lengthAdjust="spacingAndGlyphs">LARCHMOOR</textPath>
      </text>
    </svg>

    <p class="year">1712</p>
    <h1 class="spirit-name">IRISH POÍTÍN</h1>

    <div class="inn-scene" role="img" aria-label="Black and cream print of the thatched Larchmoor Inn cottage beneath tall trees"></div>

    <div class="rule"></div>

    <svg class="shamrock left" viewBox="0 0 56 56" aria-hidden="true">
      <g fill="#111">
        <circle cx="28" cy="13" r="11"/>
        <circle cx="13" cy="28" r="11"/>
        <circle cx="43" cy="28" r="11"/>
        <circle cx="28" cy="28" r="7"/>
        <path d="M26 32 Q29 44 25 55 L29 55 Q32 44 30 32 Z"/>
      </g>
    </svg>
    <p class="company-name">THE LARCHMOOR WHISKEY COMPANY</p>
    <p class="company-place">COUNTY DUNMARA, IRELAND</p>
    <svg class="shamrock right" viewBox="0 0 56 56" aria-hidden="true">
      <g fill="#111">
        <circle cx="28" cy="13" r="11"/>
        <circle cx="13" cy="28" r="11"/>
        <circle cx="43" cy="28" r="11"/>
        <circle cx="28" cy="28" r="7"/>
        <path d="M26 32 Q29 44 25 55 L29 55 Q32 44 30 32 Z"/>
      </g>
    </svg>
  </div>
</body>
</html>
```